Business card design needed

Need a business card for a new Company in Melbourne called Bright Lending Paths. This company is a Mortgage Brokering company that facilitates mainly Residential loans, but also Business and Commercial loans.
I would like something professional as I am in the finance industry.
I would like Bright Lending font wise to be bigger than paths, with the word paths to sit below the Bright Lending.

Industry/Entity Type

Finance

Contact Information for Business Card

Daniel Ostravik | Lending Specialist
Bright Lending Paths
P.O Box 617 Halsey Vic.3092
T. +61 3 9476 2153 | F. +61 3 9581 6734| M. +61 427680341
www.brightlending.com.au

Daniel Ostravik is a credit representative (CRN 572914)of KRTVE Pty.Ltd (Australian Credit Licence No 846502)

Requirements
Must have
• Daniel Ostravik is a credit representative (CRN 572914)of KRTVE Pty.Ltd (Australian Credit Licence No 846502) has to sit at the bottom of the card, in the smallest readable font.

The logo to be designed is the most crucial thing for me.

```html
<!DOCTYPE html>
<html lang="en">
<head>
<meta charset="utf-8">
<title>Bright Lending Paths – Business Card</title>
<link rel="stylesheet" href="https://fonts.googleapis.com/css2?family=Bebas+Neue&family=Roboto:wght@700&display=swap">
<style>
  :root {
    --card-blue: #0159a9;
    --name-white: #ffffff;
    --soft-blue: #5d90c2;
  }
  html, body {
    margin: 0;
    padding: 0;
    width: 1200px;
    height: 693px;
    overflow: hidden;
    background: var(--card-blue);
  }
  .card {
    position: relative;
    width: 1200px;
    height: 693px;
    background: var(--card-blue);
  }
  .brand {
    position: absolute;
    left: 50%;
    top: 222px;
    transform: translateX(-50%);
    display: flex;
    flex-direction: column;
    align-items: flex-end;
    font-family: "Bebas Neue", "Oswald", sans-serif;
    color: var(--name-white);
    font-weight: 400;
    line-height: 1;
  }
  .brand-main {
    font-size: 136px;
    letter-spacing: 2px;
    white-space: nowrap;
  }
  .brand-sub {
    font-size: 64px;
    letter-spacing: 3px;
    margin-top: -6px;
  }
  .web-address {
    position: absolute;
    left: 0;
    right: 0;
    top: 500px;
    text-align: center;
    font-family: "Roboto", Arial, sans-serif;
    font-weight: 700;
    font-size: 30px;
    color: var(--soft-blue);
    margin: 0;
  }
</style>
</head>
<body>
  <main class="card">
    <div class="brand" aria-label="Bright Lending Paths">
      <span class="brand-main">BRIGHT LENDING</span>
      <span class="brand-sub">PATHS</span>
    </div>
    <p class="web-address">www.brightlending.com.au</p>
  </main>
</body>
</html>
```